Ridgely Forge business card for handing simple contact information and generating service awareness

Utilizing the attached logo(s), generate a professional, but approachable, card conveying a sense of capability and integrity. Please only use one logo of the four attached; the different colors are all acceptable, but preference will be given to a design integrating a teal/turquoise logo,

I do not know where to put in the contact information or details?

Target Market(s)

Agriculture, Farming, Timber, Forestry, Construction, Crane Service

Industry/Entity Type

Contact Information for Business Card

Name, Phone Number, email address

Colors

Designer to choose colors to be used in the design.

Requirements
Nice to have
• It would be great to have either a mountain or one of the attached cranes as a backdrop on the rear of the card. Simple watermarks and/or Debossing is also great

```html
<!DOCTYPE html>
<html lang="en">
<head>
<meta charset="utf-8">
<title>Ridgely Forge – Business Card</title>
<link href="https://fonts.googleapis.com/css2?family=Montserrat:wght@400;600;700;800&display=swap" rel="stylesheet">
<style>
  :root {
    --backdrop: #95999c;
    --card-green: #2d6e63;
    --ink-white: #ffffff;
    --emblem-tint: #5f8f86;
  }
  * { box-sizing: border-box; margin: 0; padding: 0; }
  html, body {
    width: 1200px; height: 1200px; overflow: hidden;
    background: var(--backdrop);
    font-family: "Montserrat", Arial, sans-serif;
    color: var(--ink-white);
  }
  .card {
    position: absolute;
    left: 291px;
    width: 618px;
    height: 400px;
    background: var(--card-green);
  }
  .card--front { top: 150px; }
  .card--back { top: 650px; }

  .brand-mark {
    position: absolute;
    left: 244px; top: 82px;
    width: 130px; height: 130px;
    border-radius: 50%;
    background: var(--emblem-tint);
  }
  .brand-name {
    position: absolute;
    left: 0; right: 0; top: 225px;
    text-align: center;
    font-weight: 800;
    font-size: 38px;
    letter-spacing: 1px;
    line-height: 46px;
  }
  .brand-tagline {
    position: absolute;
    left: 0; right: 0; top: 287px;
    text-align: center;
    font-weight: 700;
    font-size: 14px;
    letter-spacing: 2.5px;
  }
  .brand-est {
    position: absolute;
    left: 0; right: 0; top: 308px;
    text-align: center;
    font-weight: 600;
    font-size: 11px;
    letter-spacing: 5px;
  }

  .contact-person {
    position: absolute;
    right: calc(618px - 244px);
    top: 180px;
    text-align: right;
  }
  .contact-person__name {
    font-weight: 600;
    font-size: 21px;
    letter-spacing: 0.5px;
    line-height: 1.1;
  }
  .contact-person__role {
    font-weight: 400;
    font-size: 15px;
    margin-top: 3px;
  }
  .contact-divider {
    position: absolute;
    left: 267px; top: 161px;
    width: 1.5px; height: 75px;
    background: var(--ink-white);
  }
  .contact-list {
    position: absolute;
    left: 298px; top: 166px;
    list-style: none;
  }
  .contact-list__item {
    display: flex; align-items: center;
    height: 23.5px;
    font-size: 15.5px;
    font-weight: 400;
  }
  .contact-list__icon {
    width: 20px; height: 18px;
    margin-right: 15px;
    flex: none;
  }
</style>
</head>
<body>
  <section class="card card--front">
    <div class="brand-mark" aria-hidden="true"></div>
    <div class="brand-name">RIDGELY FORGE</div>
    <div class="brand-tagline">TIMBER AND TRACTORS</div>
    <div class="brand-est">— EST. 2024 —</div>
  </section>

  <section class="card card--back">
    <div class="contact-person">
      <div class="contact-person__name">DALE HARROW</div>
      <div class="contact-person__role">(Founder)</div>
    </div>
    <div class="contact-divider"></div>
    <ul class="contact-list">
      <li class="contact-list__item">
        <svg class="contact-list__icon" viewBox="0 0 20 18" aria-hidden="true">
          <path d="M1 6 C1 2 19 2 19 6 L15 7 L14 4.5 L6 4.5 L5 7 Z" fill="#fff"/>
          <path d="M4 9 L7 6 L13 6 L16 9 L16 15 L4 15 Z" fill="#fff"/>
          <circle cx="10" cy="11" r="2" fill="#2d6e63"/>
        </svg>
        503-555-0142
      </li>
      <li class="contact-list__item">
        <svg class="contact-list__icon" viewBox="0 0 20 18" aria-hidden="true">
          <rect x="1" y="3" width="18" height="12" fill="#fff"/>
          <path d="M1.5 3.5 L10 10 L18.5 3.5 M1.5 14.5 L8 8.5 M18.5 14.5 L12 8.5" stroke="#2d6e63" stroke-width="1.3" fill="none"/>
        </svg>
        hello@ridgelyforge.com
      </li>
      <li class="contact-list__item">
        <svg class="contact-list__icon" viewBox="0 0 20 18" aria-hidden="true">
          <circle cx="9" cy="9" r="7.5" stroke="#fff" stroke-width="1.6" fill="none"/>
          <ellipse cx="9" cy="9" rx="3.2" ry="7.5" stroke="#fff" stroke-width="1.3" fill="none"/>
          <path d="M1.5 9 H16.5 M3 5 H15 M3 13 H15" stroke="#fff" stroke-width="1.3"/>
          <path d="M11 9 L11 18 L13.2 15.8 L15 19 L16.5 18.2 L14.8 15 L17.5 15 Z" fill="#fff" stroke="#2d6e63" stroke-width="0.8"/>
        </svg>
        www.ridgelyforge.com
      </li>
    </ul>
  </section>
</body>
</html>
```